Business Card Upgrade

I have designed our business card using our new logo. I think it needs imporovements. We used to have two cards for our business. One card was for our software business, and the other was for our consulting business. We are now in the process of combining our websites, marketing, name, and a new logo.

Our goal is to have a really sharp professional logo. One reason I designed the card the way I did was that our Titles are sometimes long, and by separating the person's name and title, it shows up very well and the title can be adjusted no matter how long it is. Sometimes the title can be 4 or 5 words or more.

We really like our logo on black as it shows up very nice. Our PMS colors are as follows: 368C and 459C.

The Designer that will be working with us will need to deliver the following:

The front and back of the Business Card Design will need to be delivered in a high quality JPEG, and
The front and back of the Business Card Design in Illustrator Format .ai
Any fonts will need to be sent to us if they are not standard and are required to open the Illustrator file correctly.

To help us get a good idea of the card with a title, please use the title: " Director of Software Development "

NOTE: The chosen designer will be selected to design our new letterhead within 2 weeks from the closing of this contest.

To help us make sure the card design works with longer titles, please use the followign job title on the card:  

"Director of Software and Product Development"

 

ALL DESIGNERS:

1. I appreciate the different angles you are showing the cards, but please be sure and always show the direct view, so I can see the layout and what the person I hand the card will see.

2. Please do not use white.  Please use off white as I don't care for white cards and they get dirty easy and do not represent the designs well.

Dear Designers,

Please provide samples straight one as a viewer of the card will see.  Some of the angles that are presented make it impossible to tell how everything fits, and sometimes even makes areas look skewed. So, please provide a straight sample view.

Pinnacle 400 company executives such as Vice Presidents, and Directors

Software

• Professional looking Card.

Our customers are Directors, Vice Presidents, and Presidents of companies as large as Pinnacle 400 companies. The card needs to get attention wile still looking professional.

Delivery of the finished product in Illustrator Format with any fonts needed to edit the text or open the file.

The card will be a heavy stock with a soft touch coating for that silk feel.

```html
<!DOCTYPE html>
<html lang="en">
<head>
<meta charset="utf-8">
<title>Kestrel Trade – Business Card</title>
<link href="https://fonts.googleapis.com/css2?family=Figtree:wght@300;400;600&display=swap" rel="stylesheet">
<style>
  :root {
    --backdrop: #bcc9c0;
    --ink: #0a0a0a;
    --paper: #f8f5ec;
    --gold: #dccb82;
    --green: #0aa46e;
    --edge: #4a4a4a;
  }
  * { margin: 0; padding: 0; box-sizing: border-box; }
  html, body { width: 1108px; height: 1200px; overflow: hidden; }
  body {
    background: var(--backdrop);
    font-family: "Figtree", "Helvetica Neue", Arial, sans-serif;
    color: var(--ink);
    position: relative;
  }
  .card {
    position: absolute;
    left: 138px;
    width: 831px;
    height: 471px;
    background: var(--paper);
    border: 1px solid var(--edge);
  }
  .card--front { top: 110px; }
  .card--back { top: 622px; overflow: hidden; }

  .brand-tab {
    position: absolute;
    left: 230px;
    top: -4px;
    width: 369px;
    height: 214px;
  }
  .brand-tab svg { position: absolute; inset: 0; width: 100%; height: 100%; }
  .brand-name {
    position: absolute;
    left: 0; right: 0; top: 72px;
    text-align: center;
    font-weight: 600;
    font-size: 36px;
    letter-spacing: 2px;
    color: var(--gold);
  }

  .person {
    position: absolute;
    right: 437px;
    top: 258px;
    text-align: right;
  }
  .person-name {
    font-weight: 600;
    font-size: 37px;
    line-height: 1;
    letter-spacing: -0.3px;
  }
  .person-title {
    margin-top: 13px;
    font-size: 29px;
    line-height: 36px;
    font-weight: 400;
  }

  .contact {
    position: absolute;
    left: 455px;
    top: 249px;
    list-style: none;
    font-size: 27px;
    line-height: 42.5px;
    font-weight: 400;
    white-space: nowrap;
  }

  .back-art { position: absolute; inset: 0; width: 100%; height: 100%; }
  .web-address {
    position: absolute;
    left: 0; right: 0; top: 144px;
    text-align: center;
    font-weight: 300;
    font-size: 90px;
    letter-spacing: -2px;
    color: var(--gold);
  }
  .web-address .domain { color: var(--green); }
</style>
</head>
<body>

<section class="card card--front">
  <div class="brand-tab">
    <svg viewBox="0 0 400 232" preserveAspectRatio="none" aria-hidden="true">
      <path fill="var(--gold)" d="M0,223 C30,214 70,205 120,203 C260,200 340,214 400,210 C350,225 300,232 250,230 C170,228 80,215 0,224 Z"/>
      <path fill="var(--ink)" d="M0,0 H400 V210 C340,214 260,200 120,203 C70,205 30,214 0,223 Z"/>
    </svg>
    <div class="brand-name">KESTREL TRADE</div>
  </div>

  <div class="person">
    <h1 class="person-name">Nathaniel Hale</h1>
    <p class="person-title">Director of Software and<br>Product Development</p>
  </div>

  <ul class="contact">
    <li>418 Harbor Bend Road</li>
    <li>Fairhope, AL 36532</li>
    <li>251.555.0147 (Direct)</li>
    <li>nhale@ktlcorp.com</li>
  </ul>
</section>

<section class="card card--back">
  <svg class="back-art" viewBox="0 0 900 510" preserveAspectRatio="none" aria-hidden="true">
    <path fill="var(--gold)" d="M0,0 H900 V386 C840,410 760,436 650,436 C520,436 380,378 230,376 C160,376 80,398 0,420 Z"/>
    <path fill="var(--ink)" d="M0,0 H900 V386 C840,396 760,411 650,411 C520,411 380,370 230,371 C160,372 80,395 0,418 Z"/>
  </svg>
  <p class="web-address">www.<span class="domain">KTLC</span>.com</p>
</section>

</body>
</html>
```